PSD website for property company

Please read the brief thoroughly.

We are looking for a new website for a property group that does property acquisitions, property development and property management.
They buy, build and lease core inner city industrial assets in Sydney, Australia.
They also invest in residential developments.

Site menu
- Home page
- Property – sub menus include – Leasing ; Projects ; Investments ; Property Management
- Capital and finance
- About
- Contact

They like this website
https://www.verlo.com.au/

They want the site to be clean, modern and bold.
They like few colors, even black and white is OK to submit

They have a logo and style guide and useable images here:
http://www.kumet.net/temp/PelorisWeb2019.zip
The zip file is also attached to this project.
We have supplied some images to give you an idea, but we will also require you to provide at least 3 extra images from stock photos.
Use your imagination.

I am expecting a lot of similar designs, so be aware the photos you choose will be really important.
They want really 3 good stock photos used and supplied without charge.
Please not too generic, I repeat the quality of the photos is important.
You may provide several photos (but not in multiple submissions please) and we will choose the best three to be provided.

The winner will be selected on a single home page design and required to provide;
All photos use in original format without charge
A second ‘standard page’ template design based on the winning home page design

```html
<!DOCTYPE html>
<html lang="en">
<head>
<meta charset="utf-8">
<title>Peloris Property</title>
<link href="https://fonts.googleapis.com/css2?family=Inter:wght@400;500;600&display=swap" rel="stylesheet">
<style>
:root{
  --green:#4e6b2a;
  --green-soft:#f3f8ec;
  --ink:#1d1d1d;
  --muted:#6f6f6f;
  --rule:#8fb0a0;
  --footer:#2d2d2d;
  --white:#ffffff;
}
*{margin:0;padding:0;box-sizing:border-box}
html,body{width:1200px;height:3681px;overflow:hidden}
body{font-family:"Inter",Arial,sans-serif;color:var(--ink);background:var(--white);position:relative}
.abs{position:absolute}
/* hero */
.hero{left:0;top:0;width:1200px;height:638px;background:linear-gradient(180deg,#5d6a78 0%,#6f7466 45%,#5a4335 75%,#3e352f 100%)}
.hero-shade{left:0;top:0;width:1200px;height:638px;background:linear-gradient(90deg,rgba(20,20,20,.35),rgba(20,20,20,0) 60%)}
.logo{left:79px;top:44px;font-size:40px;font-weight:500;letter-spacing:9px;color:var(--white)}
.nav{top:56px;left:440px;display:flex;gap:30px;font-size:13px;color:var(--white)}
.nav-cta{left:985px;top:48px;width:135px;height:33px;border:2px solid var(--white);color:var(--white);font-size:12px;display:flex;align-items:center;justify-content:center}
.hero-title{left:79px;top:268px;color:var(--white);font-size:36px;line-height:55px;font-weight:400}
.hero-title strong{font-weight:500;font-size:44px}
.hero-btn{left:79px;top:405px;width:158px;height:31px;border:2px solid var(--white);color:var(--white);font-size:11px;display:flex;align-items:center;justify-content:center}
.dots{left:1075px;top:276px;display:flex;flex-direction:column;gap:10px}
.dots span{width:10px;height:10px;border:1.5px solid var(--white);border-radius:50%}
.dots span.on{background:var(--white)}
.callbar{left:600px;top:602px;width:600px;height:77px;background:var(--green);color:var(--white);display:flex;align-items:center;padding-left:38px;font-size:18px;gap:10px}
.callbar b{font-weight:500}
.callbar .or{margin:0 24px 0 34px}
.callbar .btn{width:120px;height:34px;background:var(--white);color:var(--green);font-size:11px;display:flex;align-items:center;justify-content:center}
/* sections */
.dash{width:42px;height:2px;background:var(--rule)}
.lead{font-size:28px;line-height:38px;font-weight:400}
.copy{font-size:10px;line-height:19px;color:var(--muted)}
.outline-btn{height:31px;border:2px solid var(--green);color:var(--green);font-size:11px;font-weight:500;display:flex;align-items:center;justify-content:center}
.card{width:272px;height:350px;color:var(--white);text-align:center;display:flex;flex-direction:column;justify-content:flex-end;padding-bottom:46px}
.card h3{font-size:19px;font-weight:500}
.card p{font-size:13px;margin-top:6px}
.card.lift{justify-content:center;padding-bottom:0;box-shadow:0 20px 30px rgba(0,0,0,.25)}
.card.lift p{line-height:20px;padding:0 26px}
.card .btn{margin:22px auto 0;width:120px;height:32px;border:2px solid var(--white);font-size:11px;display:flex;align-items:center;justify-content:center}
.ph-leasing{background:linear-gradient(160deg,#a8b3b4,#8a8270 60%,#5d5443)}
.ph-invest{background:linear-gradient(170deg,#8a93a0,#6b6a6d 55%,#3f3c3a)}
.ph-manage{background:linear-gradient(160deg,#b2b8b6,#8e9288 60%,#5f6259)}
.ph-tower{background:linear-gradient(180deg,#b9c8d6 0%,#9fb1c0 35%,#6b4d3e 60%,#4a3a33 100%)}
.ph-slide{background:linear-gradient(180deg,#b8c6d2 0%,#a9a8a2 45%,#6b6357 75%,#5a6b3e 100%)}
.ph-side{background:linear-gradient(180deg,#eef0f0,#d9dbd6)}
.slide-cap{left:300px;top:2548px;width:600px;text-align:center;color:var(--white)}
.slide-cap h4{font-size:19px;font-weight:500}
.slide-cap p{font-size:13px;margin-top:6px}
.arrow{width:30px;height:30px}
/* form */
.form{left:600px;top:2756px;width:440px;height:479px;background:var(--green-soft);padding:40px 40px 0}
.field{height:40px;background:var(--white);margin-bottom:18px;font-size:10px;color:#8a8a8a;padding:0 24px;display:flex;align-items:center;justify-content:space-between}
.field.area{height:110px;align-items:flex-start;padding-top:16px}
.submit{height:41px;background:var(--green);color:var(--white);font-size:11px;font-weight:500;display:flex;align-items:center;justify-content:space-between;padding:0 24px}
/* footer */
.footer{left:0;top:3356px;width:1200px;height:325px;background:var(--footer);color:var(--white)}
.f-h{font-size:13px;font-weight:500}
.f-small{font-size:11px;line-height:24px;color:#d8d8d8}
.social{display:flex;gap:13px}
.social span{width:30px;height:30px;border:2px solid var(--green);border-radius:50%}
.social span.on{background:var(--green)}
.top-btn{width:30px;height:30px;border-radius:50%;background:var(--green)}
</style>
</head>
<body>

<header>
  <div class="abs hero" role="img" aria-label="Photo of a brick building with arched windows and trees at dusk"></div>
  <div class="abs hero-shade"></div>
  <div class="abs logo">PELORIS</div>
  <nav class="abs nav"><span>-- Home --</span><span>Property</span><span>Capital and Finance</span><span>About Us</span><span>Contact Us</span></nav>
  <div class="abs nav-cta">Enqurie Now!</div>
  <h1 class="abs hero-title">Your Personality. Your Space.<br><strong>Our Inspiraton.</strong></h1>
  <div class="abs hero-btn">Contact Us Today!</div>
  <div class="abs dots"><span></span><span class="on"></span><span></span><span></span><span></span></div>
  <div class="abs callbar">
    <span>Call Today!</span>
    <svg width="16" height="16" viewBox="0 0 24 24" fill="none" stroke="#fff" stroke-width="2"><path d="M5 3h4l2 5-3 2a12 12 0 0 0 6 6l2-3 5 2v4a2 2 0 0 1-2 2A17 17 0 0 1 3 5a2 2 0 0 1 2-2z"/></svg>
    <b>555 018 2046</b><span class="or">or</span><span class="btn">Contact Us</span>
  </div>
</header>

<section class="services">
  <div class="abs dash" style="left:79px;top:812px"></div>
  <h2 class="abs lead" style="left:160px;top:790px;width:740px">There are many variations of passages work lorem Ipsum available, but the majority have lorem suffered alteration some injected</h2>
  <div class="abs card ph-leasing" style="left:160px;top:962px" role="img" aria-label="Photo of a modern lounge interior"><h3>Leasing</h3><p>Contrary to popular</p></div>
  <div class="abs card lift ph-invest" style="left:464px;top:962px" role="img" aria-label="Photo of a modern building facade"><h3>Investments</h3><p>Contrary to popular belief, lorem Ipsum is not simply random text ...</p><span class="btn">Read More</span></div>
  <div class="abs card ph-manage" style="left:767px;top:962px" role="img" aria-label="Photo of an office foyer"><h3>Property Management</h3><p>Contrary to popular</p></div>
</section>

<section class="about">
  <div class="abs dash" style="left:79px;top:1521px"></div>
  <h2 class="abs lead" style="left:160px;top:1499px;width:380px">Contrary to popular lorem Ipsum is not simply random text</h2>
  <p class="abs copy" style="left:160px;top:1640px;width:290px">Lorem ipsum dolor sit amet, consectetur adipisicing elit. Alias voluptate ad velit perspic iatis ipsa! nostrum voluptate ex at laborum esse culpa modi, molestiae eveniet numquam tenetur expedita quis aspernatur doloribus! lorem ipsum dolor sit amet ...</p>
  <div class="abs outline-btn" style="left:160px;top:1794px;width:120px">About Us</div>
  <div class="abs ph-tower" style="left:600px;top:1433px;width:600px;height:479px" role="img" aria-label="Photo of a tall brick apartment building on a street corner"></div>
</section>

<section class="work">
  <div class="abs dash" style="left:79px;top:2046px"></div>
  <h2 class="abs lead" style="left:160px;top:2024px;width:720px">Take a look at our work. We value classic design and creative solutions.</h2>
  <div class="abs ph-side" style="left:0;top:2157px;width:269px;height:478px" role="img" aria-label="Faded photo of an arched brick building"></div>
  <div class="abs ph-slide" style="left:300px;top:2157px;width:600px;height:478px" role="img" aria-label="Photo of a building with arched ground floor and a park"></div>
  <div class="abs ph-side" style="left:933px;top:2157px;width:267px;height:478px" role="img" aria-label="Faded photo of a building with a tall arched window"></div>
  <div class="abs slide-cap"><h4>Contrary to popular belief, lorem</h4><p>majority have suffered work</p></div>
  <svg class="abs arrow" style="left:106px;top:2382px" viewBox="0 0 30 30"><path d="M18 8l-7 7 7 7" fill="none" stroke="var(--green)" stroke-width="2.5"/></svg>
  <svg class="abs arrow" style="left:1065px;top:2382px" viewBox="0 0 30 30"><path d="M12 8l7 7-7 7" fill="none" stroke="var(--green)" stroke-width="2.5"/></svg>
</section>

<section class="contact">
  <div class="abs dash" style="left:79px;top:2910px"></div>
  <h2 class="abs lead" style="left:160px;top:2886px;width:360px">Have a question or look-ing for advice?</h2>
  <p class="abs copy" style="left:160px;top:2968px;width:250px">There are many variations of passages of Lorem Ipsum available, but the majority have suffered alteration some</p>
  <div class="abs outline-btn" style="left:160px;top:3069px;width:120px">Contact Us</div>
  <form class="abs form">
    <div class="field">Name</div>
    <div class="field">Email</div>
    <div class="field">Phone</div>
    <div class="field">I'm interested in <span>&#8594;</span></div>
    <div class="field area">Message ...</div>
    <div class="submit">Enqurie Now! <span>&#8594;</span></div>
  </form>
</section>

<footer class="abs footer">
  <div class="abs f-h" style="left:160px;top:78px">Contact Us</div>
  <div class="abs" style="left:160px;top:104px;font-size:18px;display:flex;gap:8px;align-items:center">Call Today!
    <svg width="15" height="15" viewBox="0 0 24 24" fill="none" stroke="#fff" stroke-width="2"><path d="M5 3h4l2 5-3 2a12 12 0 0 0 6 6l2-3 5 2v4a2 2 0 0 1-2 2A17 17 0 0 1 3 5a2 2 0 0 1 2-2z"/></svg>
    555-018-3391</div>
  <div class="abs f-small" style="left:160px;top:128px">e. info@peloris.com</div>
  <div class="abs f-small" style="left:160px;top:168px;line-height:20px">Location:<br>48 Harbour Lane, Alexandria, Sydney,<br>2015 Australia</div>
  <div class="abs f-h" style="left:600px;top:78px">Qucik Link</div>
  <div class="abs f-small" style="left:600px;top:100px">Home<br>Property<br>Capital and Finance<br>About Us<br>Contact Us</div>
  <div class="abs f-h" style="left:799px;top:78px">© 2019 Peloris Property.</div>
  <div class="abs f-small" style="left:799px;top:98px">All Rights Reserved.</div>
  <div class="abs social" style="left:799px;top:162px"><span></span><span class="on"></span><span></span><span></span></div>
  <div class="abs top-btn" style="left:1065px;top:75px"><svg width="30" height="30" viewBox="0 0 30 30"><path d="M10 17l5-5 5 5z" fill="#fff"/></svg></div>
</footer>

</body>
</html>
```